Design Large Inspirational Artwork with Long Quote

Design a large piece of art with a quote from Marcus Hallwell.

QUOTE
"The thing that's so interesting about being alive is that you're all in. No matter what you do, you're all in. This is gonna kill you, so I think you might as well play the most magnificent game you can while you're waiting. Because, do you have anything better to do? Why not pick the best thing possible that you could do? Because you're more powerful than you think, way more powerful than you think. I mean, God only knows what you are in the final analysis. You're blind to your own weaknesses, but you're also blind to your own strengths. How far could you take that if you stopped wasting time, and if you stopped lying, and if you oriented yourself to the highest possible good that you could conceive of and you committed to that? How much good could you do? Well, I would say: why don't you find out?"

SIZE
A high-resolution print size of 6' wide and 3' tall should provide ample space for both the quote and the accompanying artwork.

TYPOGRAPHY
Choose a bold, clean, and easily readable font for the quote. You could also experiment with different font sizes for certain words or phrases to emphasize their importance within the quote.

COLORS
Since the quote is thought-provoking and reflective, you might want to use a color palette that evokes a sense of introspection and depth. Consider using cool, calming colors like shades of blue, gray, or green. Alternatively, you can use a contrasting color scheme with a light background and dark text to make the quote stand out.

ARTWORK
Select / create / edit background artwork to complement the quote.
While a great design might be minimalistic and/or greyscale, I'd really like to see some full color options. This might be anything from photography or graphics inspired by the ideas in the text, to abstract colors or illustrations that feel like the sentiment expressed.
The art should capture your attention and encourage you to read the text. The art should be visually appealing, both at a distance and up close, regardless of whether the text is read.
Updates

Having trouble confirming the exact print size.

Still looking for printing solution and final size confirmation.

Target Market(s)

Personal, business, office

Industry/Entity Type

None

Font styles to use
Sans Serif
Script

Requirements
Must have
• Entire quote, legible text, modern design, attractive artwork, approx 6ft wide and 3ft tall
Nice to have
• Different font (sizes) for certain words or phrases to emphasize their importance within the quote.

```html
<!DOCTYPE html>
<html lang="en">
<head>
<meta charset="utf-8">
<title>All In — Quote Artwork</title>
<link rel="stylesheet" href="https://fonts.googleapis.com/css2?family=Libre+Baskerville:wght@400;700&family=Playfair+Display:wght@400;600;700&display=swap">
<style>
  :root {
    --sky: #0298db;
    --ink: #ffffff;
    --pale: #93d5f5;
    --ribbon-ink: #1d78ad;
    --shadow: rgba(0, 40, 80, 0.45);
  }
  html, body {
    margin: 0;
    padding: 0;
    width: 1200px;
    height: 602px;
    overflow: hidden;
    background: var(--sky);
  }
  .artwork {
    display: block;
    width: 1200px;
    height: 602px;
    background: var(--sky);
  }
  .quote text {
    fill: var(--ink);
    font-family: "Libre Baskerville", Georgia, serif;
    filter: drop-shadow(2px 2px 2px var(--shadow));
  }
  .quote .narrow { font-family: "Playfair Display", Georgia, serif; }
  .quote .strong { font-weight: 700; }
  .quote .ribbon-text { fill: var(--ribbon-ink); filter: drop-shadow(1px 1px 0 rgba(255,255,255,0.6)); }
  .quote .closing { fill: var(--pale); }
  .ribbon { fill: var(--pale); }
  .frame { fill: none; stroke: var(--pale); stroke-width: 2.5; filter: drop-shadow(2px 2px 2px var(--shadow)); }
</style>
</head>
<body>
<svg class="artwork quote" viewBox="0 0 1200 602" width="1200" height="602" role="img" aria-label="Quote by Marcus Hallwell: The thing that's so interesting about being alive is that you're all in.">
  <!-- opening ribbon -->
  <polygon class="ribbon" points="52,90 604,90 590,123 52,123 68,106.5"/>
  <text class="ribbon-text" x="82" y="116" font-size="28" textLength="500" lengthAdjust="spacingAndGlyphs">The thing that's so interesting about being</text>

  <!-- headline word -->
  <text class="narrow" x="590" y="151" font-size="84" font-weight="400" textLength="172" lengthAdjust="spacingAndGlyphs">ALIVE</text>

  <rect class="frame" x="769" y="95" width="110" height="59"/>
  <text class="narrow strong" x="825" y="121" font-size="20" text-anchor="middle" textLength="48" lengthAdjust="spacingAndGlyphs">is that</text>
  <text class="narrow strong" x="824" y="141" font-size="20" text-anchor="middle" textLength="95" lengthAdjust="spacingAndGlyphs">you're all in.</text>

  <text x="890" y="112" font-size="25" textLength="162" lengthAdjust="spacingAndGlyphs">This is gonna</text>
  <text class="strong" x="890" y="151" font-size="44" textLength="163" lengthAdjust="spacingAndGlyphs">kill you</text>

  <text x="71" y="151" font-size="25" textLength="487" lengthAdjust="spacingAndGlyphs">No matter what you do, <tspan class="strong" font-size="30">you're all in.</tspan></text>

  <text class="narrow" x="75" y="182" font-size="29" textLength="1069" lengthAdjust="spacingAndGlyphs">so I think you might as well play the <tspan class="strong">most magnificent game</tspan> you can, <tspan font-weight="600">while you're waiting</tspan></text>

  <text x="70" y="220" font-size="24" textLength="1085" lengthAdjust="spacingAndGlyphs">Because, <tspan class="strong" font-size="30">do you have anything better to do?</tspan> Why not pick <tspan class="strong" font-size="30">the best thing possible</tspan></text>

  <text class="strong" x="70" y="257" font-size="30" textLength="1085" lengthAdjust="spacingAndGlyphs">that you could do? <tspan font-size="36">Because you're more powerful than you think,</tspan></text>

  <text x="73" y="301" font-size="30" textLength="683" lengthAdjust="spacingAndGlyphs">way more <tspan class="strong" font-size="50">powerful than you think.</tspan></text>

  <rect class="frame" x="768" y="267" width="326" height="55"/>
  <text class="strong" x="777" y="290" font-size="19" textLength="307" lengthAdjust="spacingAndGlyphs">I mean, God only knows what</text>
  <text class="strong" x="777" y="313" font-size="19" textLength="288" lengthAdjust="spacingAndGlyphs">you are in the final analysis.</text>

  <text x="70" y="348" font-size="29" textLength="1036" lengthAdjust="spacingAndGlyphs"><tspan class="strong">You're blind to your own weaknesses</tspan><tspan class="narrow">, but you're also blind to your own </tspan><tspan class="narrow strong">strengths.</tspan></text>

  <text x="73" y="388" font-size="25" textLength="1002" lengthAdjust="spacingAndGlyphs"><tspan class="narrow">How far could you take that if you stopped </tspan><tspan class="strong" font-size="31">wasting time,</tspan> and if you stopped <tspan class="strong">lying</tspan>, and</text>

  <text x="77" y="428" font-size="27" textLength="1044" lengthAdjust="spacingAndGlyphs">if you oriented yourself to the  <tspan class="strong" font-size="31">highest possible good</tspan> that you could conceive</text>

  <text x="76" y="468" font-size="29" textLength="920" lengthAdjust="spacingAndGlyphs">of  and you committed to that?  <tspan class="strong">How much good could you do?</tspan></text>

  <text class="closing" x="175" y="518" font-size="46" textLength="794" lengthAdjust="spacingAndGlyphs">Well, I would say: <tspan class="strong">why don't you find out?</tspan></text>
</svg>
</body>
</html>
```